Letterhead Design Project

I am the new owner of an existing Accouting and Financial Planning Firm (which I have been an employee at for 3 years)
We need to change the letterhead due to a change to the company's ABN etc., so thought we would like to modernise this at the same time.
We wish to keep the existing logo so there is familiarity to the clients. As per the notes on the attached document, we are happy to remove the wording from the logo, whichever will look better.
The letterhead needs to be professional, yet modern.
I will upload our logo and the required details for the letterhead.

Industry/Entity Type

Financial

Requirements
Must have
• Logo and provided business details.

```html
<!DOCTYPE html>
<html lang="en">
<head>
<meta charset="utf-8">
<title>Halden Accountants &amp; Financial Services — Letterhead</title>
<link rel="stylesheet" href="https://fonts.googleapis.com/css2?family=Tinos:wght@700&family=Open+Sans:ital,wght@0,400;1,700&display=swap">
<style>
  :root {
    --navy: #1f3f7c;
    --orange: #e9a02c;
    --paper-light: #ffffff;
    --paper-shade: #f1f2f2;
    --ink: #2a2a2a;
  }
  html, body {
    margin: 0;
    padding: 0;
    width: 876px;
    height: 1200px;
    overflow: hidden;
  }
  .letterhead {
    position: relative;
    width: 876px;
    height: 1200px;
    background: linear-gradient(90deg, var(--paper-shade) 0%, var(--paper-light) 40%, var(--paper-shade) 100%);
    font-family: "Open Sans", Arial, sans-serif;
    color: var(--ink);
    overflow: hidden;
  }
  .corner-art {
    position: absolute;
    inset: 0;
    width: 876px;
    height: 1200px;
  }
  .brand-name {
    position: absolute;
    left: 110px;
    top: 88px;
    margin: 0;
    font-family: "Tinos", "Times New Roman", serif;
    font-weight: 700;
    font-size: 62px;
    line-height: 1;
    color: var(--navy);
    letter-spacing: 1px;
  }
  .brand-dot {
    position: absolute;
    left: 256px;
    top: 177px;
    width: 12px;
    height: 12px;
    background: var(--orange);
  }
  .firm-title {
    position: absolute;
    right: 609px;
    top: 218px;
    margin: 0;
    text-align: right;
    font-family: "Tinos", "Times New Roman", serif;
    font-weight: 700;
    font-size: 22px;
    line-height: 36px;
    color: var(--navy);
    white-space: nowrap;
  }
  .firm-dot {
    position: absolute;
    left: 256px;
    top: 368px;
    width: 12px;
    height: 12px;
    background: var(--orange);
  }
  .footer-address {
    position: absolute;
    left: 208px;
    top: 1122px;
    font-size: 15px;
    line-height: 22px;
  }
  .footer-address p, .footer-contact p { margin: 0; }
  .footer-contact {
    position: absolute;
    right: 14px;
    top: 1108px;
    text-align: right;
    font-size: 15px;
    line-height: 21px;
  }
  .footer-contact .label {
    font-weight: 700;
    font-style: italic;
  }
</style>
</head>
<body>
<main class="letterhead">
  <svg class="corner-art" viewBox="0 0 876 1200" aria-hidden="true">
    <path class="corner-band" d="M712,0 C800,30 858,95 876,195 L876,0 Z" fill="var(--navy)"/>
    <path class="corner-line" d="M676,0 C790,35 855,110 876,228" fill="none" stroke="var(--orange)" stroke-width="6"/>
    <path class="corner-band" d="M0,1012 C22,1100 92,1172 168,1200 L0,1200 Z" fill="var(--navy)"/>
    <path class="corner-line" d="M0,984 C26,1098 104,1172 204,1200" fill="none" stroke="var(--orange)" stroke-width="6"/>
  </svg>

  <p class="brand-name">HALDEN</p>
  <span class="brand-dot"></span>

  <h1 class="firm-title">HALDEN<br>ACCOUNTANTS<br>&amp; FINANCIAL<br>SERVICES</h1>
  <span class="firm-dot"></span>

  <footer>
    <div class="footer-address">
      <p>ABN : 12 345 678 901</p>
      <p>27 Merrow Lane, Bellfield, Vic, 3081</p>
      <p>PO Box 418, Carrowbrook, NSW, 2330</p>
    </div>
    <div class="footer-contact">
      <p><span class="label">Tel</span> : 02 5550 1840</p>
      <p><span class="label">Fax</span> : 02 5550 1841</p>
      <p><span class="label">Email</span> : admin@haldenaccountants.com.au</p>
      <p><span class="label">web</span> : www.haldenaccountants.com.au</p>
    </div>
  </footer>
</main>
</body>
</html>
```